Redesign Craft Brewing Recipe Website

Originally built with Bootstrap just to get the site going, I am seeking a complete redesign of the sites home page and recipe page. I am an experienced web developer with no graphic background, initially just looking for psd mocks.

I prefer styles that are clean and modern, and would prefer anything that is fun, engaging, and has an organic feel to it. I currently have a cartoon rabbit as a logo, but it needs some modification/tweaking, so any help in that area would be great as well.

Current site:
http://kettlewren.plumhostsite.net/

Current launch page/logo:
http://www.kettlewren.com/

I like the overall layout of the elements currently, but the design sucks.

The launch page is at the following URL

Reason: Still looking for a more modern design. Designs received so far are too similar to the original.

My site is content based and does not contain images or products. Your design should not consist of large images.

Reason: The website has very little images, so the designs need to be more text and content based. The header needs to be very small and should not contain an ad rotater.

Target Market(s)

Home brewers, Craft brewers, Microbreweries, Brewpubs

Requirements
Must have
• Web 2.0 Look and Feel, Fun, Hip, Focus on content
Should not have
• A large photo as a header

```html
<!DOCTYPE html>
<html lang="en">
<head>
<meta charset="utf-8">
<title>Kettlewren – Delicious beer recipes from around the world</title>
<link rel="stylesheet" href="https://fonts.googleapis.com/css2?family=Inter:wght@400;600;700;800&display=swap">
<style>
  :root {
    --page-bg: #e9e9e9;
    --ink: #222222;
    --ink-soft: #3a3a3a;
    --muted: #7a7a7a;
    --rule: #555555;
    --brand-green: #2fd88f;
    --link-blue: #2a9fd8;
    --bar-black: #141414;
    --panel-white: #ffffff;
    --panel-fade: #ececec;
    --badge-orange: #f47a1f;
    --badge-pink: #ec1763;
    --badge-purple: #9b1fd6;
    --check-border: #9a9a9a;
  }
  * { box-sizing: border-box; margin: 0; padding: 0; }
  html, body { width: 1200px; height: 825px; overflow: hidden; }
  body {
    background: var(--page-bg);
    font-family: "Inter", "Helvetica Neue", Arial, sans-serif;
    color: var(--ink);
  }
  .page { position: relative; width: 1200px; height: 825px; overflow: hidden; padding: 0 130px 0 140px; }

  /* Header */
  .site-header { position: relative; height: 96px; }
  .brand { position: absolute; left: 0; top: 44px; display: flex; align-items: center; gap: 10px; }
  .brand-dot { width: 26px; height: 26px; border-radius: 50%; background: var(--ink); }
  .brand-name { font-size: 17px; font-weight: 800; letter-spacing: 0.5px; color: var(--ink); }
  .social { position: absolute; right: 0; top: 18px; display: flex; gap: 8px; }
  .social-square { width: 20px; height: 20px; background: var(--ink-soft); border-radius: 3px; }
  .main-nav { position: absolute; right: 0; top: 52px; font-size: 11px; font-weight: 600; color: var(--ink); letter-spacing: 0.3px; }
  .main-nav span.sep { margin: 0 8px; color: var(--muted); }

  /* Hero */
  .hero { margin-top: 8px; font-size: 80px; font-weight: 700; line-height: 88px; letter-spacing: -2px; color: var(--ink); }
  .hero .accent { color: var(--brand-green); }

  /* Content grid */
  .content { display: flex; gap: 20px; margin-top: 50px; }

  /* Sidebar */
  .filters { width: 292px; flex: none; }
  .search-bar { background: var(--bar-black); height: 40px; display: flex; align-items: center; padding: 0 10px; gap: 14px; }
  .search-input { flex: 1; height: 24px; background: var(--panel-white); border: 1px solid #bbb; font-size: 11px; color: #aaa; padding: 5px 8px; }
  .search-go { width: 50px; height: 24px; border-radius: 12px; background: linear-gradient(#fafafa, #d4d4d4); font-size: 11px; font-weight: 600; text-align: center; line-height: 24px; color: var(--ink); }
  .filter-panel { margin-top: 8px; border: 8px solid var(--bar-black); background: linear-gradient(var(--panel-white), var(--panel-fade)); padding: 18px 16px 20px; }
  .filter-heading { font-size: 12px; font-weight: 700; color: var(--muted); letter-spacing: 0.4px; margin: 0 0 10px; }
  .filter-group + .filter-group { margin-top: 18px; }
  .option { display: flex; align-items: center; gap: 10px; font-size: 13px; color: var(--ink-soft); height: 26px; }
  .box { width: 14px; height: 14px; border: 1px solid var(--check-border); background: linear-gradient(#fff, #ddd); }
  .box.checked { background: var(--ink-soft); border-color: var(--ink); position: relative; }
  .box.checked::after { content: "×"; position: absolute; inset: -3px 0 0 2px; color: #fff; font-size: 13px; font-weight: 700; }
  .badge { width: 22px; height: 22px; border-radius: 50%; color: #fff; font-size: 7px; font-weight: 700; display: inline-flex; align-items: center; justify-content: center; }
  .badge.orange { background: var(--badge-orange); }
  .badge.pink { background: var(--badge-pink); }
  .badge.purple { background: var(--badge-purple); }
  .style-list { position: relative; padding-right: 22px; }
  .style-scroll { position: absolute; right: 4px; top: 6px; width: 6px; height: 176px; background: #d7d7d7; border-radius: 3px; }
  .style-scroll::after { content: ""; position: absolute; left: 0; top: 30px; width: 6px; height: 36px; background: var(--ink); border-radius: 3px; }
  .range { position: relative; height: 14px; margin: 8px 8px 0; }
  .range-track { position: absolute; left: 0; right: 0; top: 5px; height: 5px; background: #d2d2d2; border-radius: 3px; }
  .range-thumb { position: absolute; top: 0; width: 22px; height: 14px; background: var(--bar-black); border-radius: 4px; }
  .range-labels { display: flex; gap: 36px; margin: 6px 0 0 24px; font-size: 11px; color: var(--ink-soft); }

  /* Recipe cards */
  .recipes { width: 608px; flex: none; }
  .recipe + .recipe { margin-top: 26px; }
  .recipe-bar { height: 40px; background: var(--bar-black); display: flex; align-items: center; padding: 0 12px; color: #fff; }
  .recipe-title { font-size: 20px; font-weight: 700; flex: 1; letter-spacing: -0.2px; }
  .recipe-style { font-size: 9px; font-weight: 700; letter-spacing: 0.3px; margin-right: 12px; }
  .recipe-body { display: flex; justify-content: space-between; padding: 16px 12px 0; }
  .recipe-desc { width: 370px; font-size: 12px; line-height: 17px; color: var(--ink); font-weight: 600; }
  .recipe-credit { margin-top: 6px; font-size: 10.5px; font-weight: 600; }
  .recipe-credit a { color: var(--link-blue); text-decoration: none; }
  .stats { width: 170px; border-collapse: collapse; font-size: 10.5px; font-weight: 700; }
  .stats td { height: 20px; border-bottom: 1px solid var(--rule); }
  .stats td:first-child { width: 48px; padding-left: 8px; }
  .stats tr:last-child td { border-bottom: none; }
</style>
</head>
<body>
<div class="page">
  <header class="site-header">
    <div class="brand"><span class="brand-dot"></span><span class="brand-name">KETTLEWREN</span></div>
    <div class="social" aria-label="Social links"><span class="social-square"></span><span class="social-square"></span></div>
    <nav class="main-nav">RECIPES<span class="sep">|</span>LOG IN</nav>
  </header>

  <h1 class="hero">The easiest way to<br><span class="accent">create and share</span><br>craft beer recipes_</h1>

  <div class="content">
    <aside class="filters">
      <div class="search-bar"><div class="search-input">Search</div><div class="search-go">Go!</div></div>
      <div class="filter-panel">
        <div class="filter-group">
          <h2 class="filter-heading">BREWING</h2>
          <div class="option"><span class="box"></span>Extract<span class="badge orange">P/M</span></div>
          <div class="option"><span class="box"></span>Partial Mash<span class="badge pink">E</span></div>
          <div class="option"><span class="box"></span>All Grain<span class="badge purple">A/G</span></div>
        </div>
        <div class="filter-group">
          <h2 class="filter-heading">STYLES</h2>
          <div class="style-list">
            <span class="style-scroll"></span>
            <div class="option"><span class="box"></span>American Amber Ale</div>
            <div class="option"><span class="box"></span>American Barleywine</div>
            <div class="option"><span class="box"></span>American Brown Ale</div>
            <div class="option"><span class="box"></span>American IPA</div>
            <div class="option"><span class="box"></span>American Pale Ale</div>
            <div class="option"><span class="box"></span>American Stout</div>
            <div class="option"><span class="box"></span>American Brown Ale</div>
          </div>
        </div>
        <div class="filter-group">
          <h2 class="filter-heading">MATCH MAKER</h2>
          <div class="option"><span class="box checked"></span>Boil Size</div>
          <div class="range"><span class="range-track"></span><span class="range-thumb" style="left:18px"></span><span class="range-thumb" style="left:72px"></span></div>
          <div class="range-labels"><span>2 GAL</span><span>5 GAL</span></div>
        </div>
      </div>
    </aside>

    <main class="recipes">
      <article class="recipe">
        <div class="recipe-bar"><h3 class="recipe-title">Venom Belgian Specialty Ale</h3><span class="recipe-style">BELGIAN SPECIALTY ALE</span><span class="badge orange">P/M</span></div>
        <div class="recipe-body">
          <div>
            <p class="recipe-desc">Lorem ipsum dolor sit amet, consectetur adipisicing elit, sed do eiusmoectetur adid tempor incididunt ut labore et dolore magna ali ectetur adipisicing elit, ectetur adipg elit, qua.</p>
            <p class="recipe-credit">created by <a href="#">Dana Whitfield</a></p>
          </div>
          <table class="stats"><tr><td>13.93%</td><td>ABV</td></tr><tr><td>28</td><td>SRM</td></tr><tr><td>1.139</td><td>OG</td></tr><tr><td>1.036</td><td>FG</td></tr><tr><td>126</td><td>IBU</td></tr></table>
        </div>
      </article>
      <article class="recipe">
        <div class="recipe-bar"><h3 class="recipe-title">Honeysucker Traditional Bock</h3><span class="recipe-style">TRADITIONAL BOCK</span><span class="badge pink">E</span></div>
        <div class="recipe-body">
          <div>
            <p class="recipe-desc">Lorem ipsum dolor sit amet, consectetur adipisicing elit, sed do eiusmoectetur adid tempor incididunt ut labore et dolore magna ali ectetur adipisicing elit, ectetur adipg elit, qua.</p>
            <p class="recipe-credit">created by <a href="#">Dana Whitfield</a></p>
          </div>
          <table class="stats"><tr><td>13.93%</td><td>ABV</td></tr><tr><td>28</td><td>SRM</td></tr><tr><td>1.139</td><td>OG</td></tr><tr><td>1.036</td><td>FG</td></tr><tr><td>126</td><td>IBU</td></tr></table>
        </div>
      </article>
      <article class="recipe">
        <div class="recipe-bar"><h3 class="recipe-title">Venom Baltic Porter</h3><span class="recipe-style">BALTIC PORTER</span><span class="badge purple">A/G</span></div>
        <div class="recipe-body">
          <div>
            <p class="recipe-desc">Lorem ipsum dolor sit amet, consectetur adipisicing elit, sed do eiusmoectetur adid tempor incididunt ut labore et dolore magna ali ectetur adipisicing elit, ectetur adipg elit, qua.</p>
            <p class="recipe-credit">created by <a href="#">Dana Whitfield</a></p>
          </div>
          <table class="stats"><tr><td>13.93%</td><td>ABV</td></tr><tr><td>28</td><td>SRM</td></tr><tr><td>1.139</td><td>OG</td></tr><tr><td>1.036</td><td>FG</td></tr><tr><td>126</td><td>IBU</td></tr></table>
        </div>
      </article>
    </main>
  </div>
</div>
</body>
</html>
```